Roadside building business signage for a holistic health clinic.

Replace signs as shown in the attached file. They are perforated stickers that go on the windows as shown. Looking for something that has our logo and says the name of the practice with logo (Fernbrook Health & Wellness) also boldly says Acupuncture, IV Vitamins, and Holistic Health.
Possibly our phone number as well 318-627-5194
Updates

Please don't use pink except the logo. Earthy, organic tone colors appreciated.

Need of eye catching window signage of a holistic clinic on a brick building. Pink, purple, sage green, white color. Logo is pink on a white background. Please don't overload with too much pink. Words to include are "Fernbrook Health and Wellness(name of business)", "Direct Primary Care", " Medical acupuncture", "IV Vitamin Therapy", "fernbrookcare-example.com","318-627-5194".

Target Market(s)

People will see in their cars passing by the building. Busy roadside so need to be visible while passing in fast speed.

Industry/Entity Type

Health & Wellness

Font styles to use
Sans Serif

Colors

Designer to choose colors to be used in the design.

Requirements
Must have
• On sign must have words Holistic Medicine, Medical Acupuncture, Direct Primary Care and IV vitamins.
Nice to have
• Simple, minimalistic, artistic yet has clear message. White, Black, Violet, Pink (logo), Dark green, Sage green.
Should not have
• Bold colors (red, yellow, blue), same tone colors. Blue waves on the current signage (uploaded file) must go.

```html
<!DOCTYPE html>
<html lang="en">
<head>
<meta charset="utf-8">
<title>Fernbrook Health &amp; Wellness – Window Sign</title>
<link rel="stylesheet" href="https://fonts.googleapis.com/css2?family=Cinzel:wght@500&family=Oswald:wght@500;600&display=swap">
<style>
  :root {
    --frame: #000000;
    --cream: #f6f4ec;
    --pine: #1f4a38;
    --ink: #0b0b0b;
    --sage-light: #cddbc4;
    --sage: #a9c29c;
    --sage-deep: #87a67c;
    --floor: #5b5346;
    --floor-light: #7a705f;
    --blossom: #e0579b;
    --seam: #3a3a3a;
    --photo-warm: #d9a48f;
    --photo-light: #efebe2;
  }
  html, body {
    margin: 0;
    padding: 0;
    width: 1200px;
    height: 870px;
    overflow: hidden;
    background: #ffffff;
  }
  .canvas {
    position: relative;
    width: 1200px;
    height: 870px;
  }
  .window-sign {
    position: absolute;
    top: 10px;
    left: 315px;
    width: 569px;
    height: 850px;
  }
  .brand-name {
    font-family: "Cinzel", serif;
    font-weight: 500;
    fill: var(--pine);
  }
  .brand-tagline {
    font-family: "Cinzel", serif;
    font-weight: 500;
    fill: var(--pine);
  }
  .phone {
    font-family: "Oswald", sans-serif;
    font-weight: 600;
    fill: var(--ink);
  }
  .website {
    font-family: "Oswald", sans-serif;
    font-weight: 500;
    fill: var(--pine);
  }
  .service {
    font-family: "Oswald", sans-serif;
    font-weight: 600;
    fill: var(--pine);
  }
  .bullet { fill: #ffffff; }
  .seam { stroke: var(--seam); stroke-width: 1.5; fill: none; }
</style>
</head>
<body>
<main class="canvas">
  <svg class="window-sign" viewBox="0 0 967 1444" xmlns="http://www.w3.org/2000/svg" aria-label="Fernbrook Health and Wellness window sign">
    <defs>
      <clipPath id="sign-face">
        <path d="M25,32 A445,470 0 0 1 470,505 L942,505 L942,1419 L25,1419 Z"/>
      </clipPath>
      <linearGradient id="floor-shade" x1="0" y1="0" x2="0" y2="1">
        <stop offset="0" stop-color="var(--floor-light)"/>
        <stop offset="1" stop-color="var(--floor)"/>
      </linearGradient>
      <linearGradient id="portrait-tone" x1="0" y1="0" x2="0" y2="1">
        <stop offset="0" stop-color="var(--photo-light)"/>
        <stop offset="0.3" stop-color="var(--photo-warm)"/>
        <stop offset="0.75" stop-color="var(--photo-warm)"/>
        <stop offset="1" stop-color="#e6e1d8"/>
      </linearGradient>
    </defs>

    <path class="sign-frame" fill="var(--frame)" d="M0,0 A480,480 0 0 1 490,480 L967,480 L967,1444 L0,1444 Z"/>

    <g class="sign-face" clip-path="url(#sign-face)">
      <rect class="backdrop" x="0" y="0" width="967" height="1444" fill="var(--cream)"/>

      <path class="meadow meadow-light" fill="var(--sage-light)"
        d="M0,965 C160,952 300,945 480,950 C650,955 800,948 967,952 L967,1444 L0,1444 Z"/>
      <path class="meadow meadow-mid" fill="var(--sage)"
        d="M0,1085 C160,1078 320,1068 480,1072 C650,1076 800,1066 967,1070 L967,1444 L0,1444 Z"/>
      <path class="meadow meadow-deep" fill="var(--sage-deep)"
        d="M0,1330 C160,1322 320,1316 480,1320 C650,1324 800,1316 967,1320 L967,1444 L0,1444 Z"/>

      <rect class="floor" x="0" y="1372" width="967" height="72" fill="url(#floor-shade)"/>

      <rect class="portrait" role="img" aria-label="Photo of a woman meditating cross-legged"
        x="500" y="540" width="442" height="860" rx="30" fill="url(#portrait-tone)"/>

      <line class="seam" x1="25" y1="480" x2="482" y2="480"/>
      <line class="seam" x1="482" y1="480" x2="482" y2="1419"/>
      <line class="seam" x1="25" y1="962" x2="942" y2="962"/>
    </g>

    <g class="brand">
      <circle class="brand-dot" cx="250" cy="600" r="44" fill="var(--blossom)"/>
      <text class="brand-name" x="250" y="750" font-size="58" text-anchor="middle" textLength="410" lengthAdjust="spacing">FERNBROOK</text>
      <text class="brand-tagline" x="250" y="788" font-size="20" text-anchor="middle" textLength="340" lengthAdjust="spacing">HEALTH &amp; WELLNESS</text>
    </g>

    <text class="phone" x="250" y="878" font-size="54" text-anchor="middle">318-627-5194</text>
    <text class="website" x="250" y="926" font-size="28" text-anchor="middle">fernbrookcare-example.com</text>

    <g class="service-icons">
      <rect role="img" aria-label="Icon of capsules with a sprout" x="112" y="995" width="56" height="56" rx="14" fill="none" stroke="var(--pine)" stroke-width="4"/>
      <rect role="img" aria-label="Icon of a meditating figure" x="210" y="995" width="56" height="56" rx="14" fill="none" stroke="var(--pine)" stroke-width="4"/>
      <rect role="img" aria-label="Icon of a hand with acupuncture points" x="308" y="995" width="56" height="56" rx="14" fill="none" stroke="var(--pine)" stroke-width="4"/>
    </g>

    <g class="service-list">
      <circle class="bullet" cx="78" cy="1126" r="8"/>
      <text class="service" x="100" y="1140" font-size="36">IV VITAMIN THERAPY</text>
      <circle class="bullet" cx="78" cy="1184" r="8"/>
      <text class="service" x="100" y="1198" font-size="36">MEDICAL ACUPUNCTURE</text>
      <circle class="bullet" cx="78" cy="1242" r="8"/>
      <text class="service" x="100" y="1256" font-size="36">DIRECT PRIMARY CARE</text>
      <circle class="bullet" cx="78" cy="1300" r="8"/>
      <text class="service" x="100" y="1314" font-size="36">HOLISTIC MEDICINE</text>
    </g>
  </svg>
</main>
</body>
</html>
```